QM Fenwold Detailing, Inc.

I'm looking for business card design for an existing company with an existing logo/website. www.qmfenwold-detailing.com. VETERAN OWNED logo must be present.

Target Market(s)

Structural and architectural steel fabricators

Industry/Entity Type

Structural and architectural steel detailing and engineering

Contact Information for Business Card

logo, business name, address, phone, website, email, employee info

Font styles to use
Serif

Colors
00AB8E
00BBA5
67D7C9
C6EFE9
E9F9F6

Requirements
Must have
• company logo, website, VETERAN OWNED LOGO
Should not have
• Don't make it too busy. Less is more

```html
<!DOCTYPE html>
<html lang="en">
<head>
<meta charset="utf-8">
<title>QM Fenwold Detailing – Business Card</title>
<link rel="stylesheet" href="https://fonts.googleapis.com/css2?family=Josefin+Slab:wght@400;600;700&display=swap">
<style>
  :root {
    --page-bg: #e8e6e2;
    --green-deep: #00ab8e;
    --green-mid: #00bba5;
    --green-soft: #67d7c9;
    --green-pale: #c6efe9;
    --green-mist: #e9f9f6;
    --green-dark: #00705d;
    --ink: #06231e;
    --text-grey: #3a4442;
    --card-white: #f8fbfa;
  }
  * { box-sizing: border-box; margin: 0; padding: 0; }
  html, body { width: 1200px; height: 900px; overflow: hidden; }
  body {
    background: var(--page-bg);
    font-family: "Josefin Slab", serif;
    position: relative;
  }
  .card {
    position: absolute;
    left: 270px;
    width: 660px;
    height: 378px;
    border-radius: 4px;
    box-shadow: 0 8px 24px rgba(0,0,0,0.18);
    overflow: hidden;
  }

  /* Front */
  .card-front {
    top: 40px;
    background: radial-gradient(ellipse at 50% 45%, var(--green-soft) 0%, var(--green-mid) 40%, var(--green-deep) 70%, var(--green-dark) 100%);
    display: flex;
    flex-direction: column;
    align-items: center;
    justify-content: center;
    text-align: center;
    color: var(--ink);
  }
  .brand { display: flex; align-items: center; gap: 14px; }
  .brand-mark { width: 22px; height: 22px; background: var(--ink); flex: none; }
  .brand-name {
    font-weight: 700;
    font-size: 38px;
    letter-spacing: 0.04em;
    text-transform: uppercase;
    white-space: nowrap;
  }
  .services { margin-top: 46px; }
  .services-title { font-weight: 700; font-size: 19px; margin-bottom: 8px; }
  .services-text { font-size: 17px; line-height: 1.35; font-weight: 600; }

  /* Back */
  .card-back {
    top: 470px;
    background: linear-gradient(160deg, #ffffff 0%, var(--card-white) 50%, var(--green-mist) 100%);
    color: var(--text-grey);
  }
  .card-back .brand { position: absolute; right: 38px; top: 52px; }
  .card-back .brand-name { font-size: 28px; color: var(--green-deep); }
  .card-back .brand-mark { width: 16px; height: 16px; background: var(--green-deep); }

  .veteran-badge {
    position: absolute;
    right: 44px;
    top: 214px;
    width: 84px;
    height: 84px;
    border-radius: 50%;
    background: radial-gradient(circle, var(--green-pale) 0%, var(--green-soft) 100%);
    border: 3px solid var(--green-deep);
  }

  .person { position: absolute; left: 40px; top: 180px; }
  .person-name {
    font-weight: 700;
    font-size: 26px;
    color: var(--green-deep);
    text-transform: uppercase;
  }
  .person-role { font-size: 19px; margin-top: 2px; margin-left: 10px; font-weight: 600; }
  .contacts { list-style: none; margin-top: 16px; margin-left: 20px; }
  .contacts li {
    display: flex;
    align-items: center;
    gap: 10px;
    font-size: 17px;
    font-weight: 600;
    line-height: 1.45;
  }
  .contacts svg { width: 15px; height: 15px; flex: none; }
  .address-rule {
    position: absolute;
    left: 40px;
    right: 40px;
    top: 330px;
    border-top: 1.5px solid var(--green-deep);
  }
  .address {
    position: absolute;
    left: 40px;
    top: 341px;
    font-size: 17px;
    font-weight: 600;
    white-space: nowrap;
  }
</style>
</head>
<body>

<section class="card card-front">
  <div class="brand">
    <span class="brand-mark"></span>
    <span class="brand-name">QM Fenwold Detailing</span>
  </div>
  <div class="services">
    <p class="services-title">Our Services</p>
    <p class="services-text">We Offer a Wide Range of Structural &amp;<br>Architectural Steel Detailing Services.</p>
  </div>
</section>

<section class="card card-back">
  <div class="brand">
    <span class="brand-mark"></span>
    <span class="brand-name">QM Fenwold Detailing</span>
  </div>

  <div class="veteran-badge" role="img" aria-label="Veteran owned business badge"></div>

  <div class="person">
    <p class="person-name">Daniel Marsh</p>
    <p class="person-role">Director</p>
    <ul class="contacts">
      <li>
        <svg viewBox="0 0 16 16" aria-hidden="true"><path fill="#00ab8e" d="M3.6 1.5l2.3 2.6-1.3 1.6c.9 2 2.6 3.7 4.6 4.6l1.6-1.3 2.6 2.3-1.5 2.2C6.5 13.3 2.7 9.5 1.5 3.1z"/></svg>
        555.210.4817
      </li>
      <li>
        <svg viewBox="0 0 16 16" aria-hidden="true"><rect x="1" y="3" width="14" height="10" fill="#00ab8e"/><path d="M1 3l7 6 7-6" fill="none" stroke="#fff" stroke-width="1.3"/></svg>
        sales@qmfenwold-detailing.com
      </li>
      <li>
        <svg viewBox="0 0 16 16" aria-hidden="true"><g fill="none" stroke="#00ab8e" stroke-width="1.2"><circle cx="8" cy="8" r="6.5"/><ellipse cx="8" cy="8" rx="3" ry="6.5"/><path d="M1.5 8h13M2.5 4.8h11M2.5 11.2h11"/></g></svg>
        www.qmfenwold-detailing.com
      </li>
    </ul>
  </div>

  <div class="address-rule"></div>
  <p class="address">QM Fenwold Detailing 4810 Harbor Crest Ave. ste 300, Larkfield, FL 33990</p>
</section>

</body>
</html>
```